Create a Landing Page Design

I need a landing page designed and coded in HTML for tallbrook.com that follows an "F" pattern design.

Examples:

Quillhaven: https://www.quillhaven.com/form/sem/sales_software.jsp?d=00000000000abcD1
Jar: https://app.jar.com/signup/o/sendlargefiles?kw=jar%20cloud%20storage
Ravenlisk: http://www.ravenlisk.com/Landing-Templates/Demo/?Campaign_ID=00000000000Abcd
Plumvane: http://pages2.plumvane.com/PPC-MarketingAutomationforLife.html?source=PPC&comment=PPC_GS_US
Cobaltbay: http://cobaltbay.com/free-helpdesk-software
Loom: http://help.loomly-example.com/free-trial?source1=CPC-Freetrial

It needs:

- Bullet point content to the left
- Sign-up form to the right (with image) - we'll provide the code for this
- Testimonials underneath
- A "human" image that conveys that there are people behind the brand. Here's a link to a vantorel folder of stock images we've purchased on this theme: https://files.vantorel.com/sh/ab12cd34ef56gh/x9yZ8wV7

I've attached a simple Sketchpine wireframe so you understand what we're looking for.

We'd like to use our existing (https://tallbrook.com/) header and footer, but remove all links (other than privacy policy + terms of service).

Thanks!

```html
<!DOCTYPE html>
<html lang="en">
<head>
<meta charset="utf-8">
<title>Tallbrook – Free Membership</title>
<link rel="stylesheet" href="https://fonts.googleapis.com/css2?family=Ubuntu:ital,wght@0,400;0,500;1,400&family=Open+Sans:wght@400;600&display=swap">
<style>
  :root{
    --ink:#3a3a3a;
    --grey:#7b7b7b;
    --topbar:#232325;
    --blue-deep:#1189b4;
    --blue:#2ab8e0;
    --blue-light:#44d0f5;
    --blue-line:#0f79a3;
    --accent:#1a8cc0;
    --form-title:#0f73a8;
    --field:#f4f4f4;
    --field-border:#dcdcdc;
    --strip:#e8e8e8;
    --footer:#2a2a2c;
    --footer-text:#6d6d6f;
  }
  *{box-sizing:border-box;margin:0;padding:0}
  html,body{width:1200px;height:1100px;overflow:hidden;background:#fff}
  body{position:relative;font-family:"Open Sans",Arial,sans-serif;color:var(--ink)}
  .topbar{position:absolute;left:0;top:0;width:1200px;height:6px;background:var(--topbar)}

  .site-header{position:absolute;left:0;top:6px;width:1200px;height:109px;background:#fff}
  .brand{position:absolute;left:100px;top:16px;display:flex;align-items:center;gap:14px}
  .brand-mark{width:76px;height:76px;border-radius:50%;background:#f0a030}
  .brand-name{font-family:"Ubuntu",sans-serif;font-size:29px;color:#8a8a8a}
  .social{position:absolute;right:100px;top:39px;display:flex;gap:13px}
  .social span{width:38px;height:38px;border-radius:50%;display:block}
  .social .s1{background:#3a66b0}.social .s2{background:#37b0e6}.social .s3{background:#444}.social .s4{background:#1d7dbf}

  .hero{position:absolute;left:0;top:115px;width:1200px;height:618px;
    border-top:4px solid var(--blue-line);border-bottom:4px solid var(--blue-line);
    background:radial-gradient(ellipse 420px 300px at 330px 560px,var(--blue-light),transparent),
               radial-gradient(ellipse 380px 260px at 1120px 650px,var(--blue-light),transparent),
               radial-gradient(ellipse 300px 200px at 560px 80px,#34c4ea,transparent),
               linear-gradient(90deg,var(--blue-deep),var(--blue) 45%,var(--blue-deep) 80%,var(--blue))}
  .hero-title{position:absolute;left:103px;top:16px;font-family:"Ubuntu",sans-serif;font-weight:500;font-size:45px;color:#fff;letter-spacing:1px}
  .hero-sub{position:absolute;left:106px;top:68px;font-family:"Ubuntu",sans-serif;font-size:21px;color:#fff}
  .hero-photo{position:absolute;left:101px;top:116px;width:452px;height:226px;border:1px solid #0d6e92;
    background:linear-gradient(100deg,#9aa3a6,#c79b80 40%,#8a90a8 70%,#d6d9dc)}
  .benefits{position:absolute;left:101px;top:363px;list-style:none}
  .benefit{position:relative;padding-left:56px;margin-bottom:0}
  .benefit-icon{position:absolute;left:0;top:2px;width:43px;height:43px;border-radius:50%;background:#b9ecfa;display:flex;align-items:center;justify-content:center}
  .benefit h3{font-family:"Ubuntu",sans-serif;font-weight:400;font-size:18px;color:#e8fbff;line-height:26px}
  .benefit p{font-size:10px;line-height:15px;color:#d4f3fc;width:350px;margin-top:3px;letter-spacing:-.2px}
  .b1{height:87px}.b2{height:79px}

  .signup{position:absolute;left:635px;top:74px;width:466px;height:430px}
  .signup-frame{position:absolute;inset:0}
  .signup-inner{position:absolute;left:0;top:0;width:466px;height:430px}
  .signup-close{position:absolute;right:12px;top:10px;font-size:18px;font-weight:600;color:var(--form-title);line-height:1}
  .signup-title{position:absolute;left:36px;top:34px;font-family:"Ubuntu",sans-serif;font-weight:500;font-size:17px;color:var(--form-title)}
  .signup-lead{position:absolute;left:36px;top:66px;width:397px;font-size:13px;line-height:20px;color:#444}
  .signup-lead span{display:block;border-bottom:1px solid #e4e4e4}
  .field{position:absolute;left:99px;width:271px;height:45px;border:1px solid var(--field-border);border-radius:3px;background:var(--field);
    font-size:13px;color:#8d8d8d;padding:13px 0 0 31px}
  .field svg{position:absolute;right:16px;top:15px}
  .f1{top:143px}.f2{top:198px}.f3{top:253px}
  .choice{position:absolute;left:104px;font-size:13px;color:#444;display:flex;align-items:center;gap:7px}
  .choice i{width:12px;height:12px;border:1px solid #3c6f90;border-radius:50%;display:block}
  .c1{top:310px}.c2{top:335px}
  .submit{position:absolute;left:164px;top:378px;width:140px;height:36px;border-radius:18px;border:1px solid #a8a8a8;
    background:linear-gradient(#e2e2e2,#b9b9b9);font-family:"Ubuntu",sans-serif;font-size:17px;color:#333;text-align:center;line-height:34px}

  .testimonial{position:absolute;left:100px;top:755px;width:420px;height:140px}
  .quote-open,.quote-close{position:absolute;font-family:Georgia,serif;font-size:60px;color:#cfcfcf;line-height:1;font-weight:700}
  .quote-open{left:0;top:0}.quote-close{left:352px;top:100px}
  .avatar{position:absolute;left:43px;top:25px;width:60px;height:60px;border-radius:50%;background:linear-gradient(#e4e4e4,#bdbdbd);border:1px solid #ddd}
  .quote-text{position:absolute;left:120px;top:18px;width:290px;font-style:italic;font-size:15px;line-height:22px;color:#666}
  .quote-author{position:absolute;left:120px;top:93px;font-style:italic;font-size:15px;color:var(--accent)}

  .abtest{position:absolute;left:628px;top:741px;width:380px}
  .abtest h2{font-family:"Ubuntu",sans-serif;font-weight:400;font-size:17px;color:#333}
  .abtest .tag{font-size:10px;color:#777;margin-top:6px}
  .steps{position:absolute;left:0;top:46px}
  .step-label{position:absolute;font-size:9px;color:#333;white-space:nowrap}

  .partners{position:absolute;left:0;top:953px;width:1200px;height:48px;background:var(--strip);
    display:flex;align-items:center;font-family:"Ubuntu",sans-serif;color:#666}
  .partners span{position:absolute;top:12px;font-size:20px}

  .site-footer{position:absolute;left:0;top:1001px;width:1200px;height:99px;background:var(--footer)}
  .footer-rule{position:absolute;left:106px;top:44px;width:679px;height:1px;background:#444}
  .copyright{position:absolute;left:106px;top:59px;font-size:11px;color:var(--footer-text)}
  .copyright a{color:var(--footer-text)}
  .footer-brand{position:absolute;left:810px;top:26px;display:flex;align-items:center;gap:10px}
  .footer-brand i{width:48px;height:56px;background:#e55a2b;display:block;border-radius:4px}
  .footer-brand span{font-family:"Ubuntu",sans-serif;font-size:29px;color:#9a9a9a}
</style>
</head>
<body>
<div class="topbar"></div>

<header class="site-header">
  <div class="brand"><span class="brand-mark"></span><span class="brand-name">Tallbrook</span></div>
  <nav class="social" aria-label="Social profiles">
    <span class="s1" aria-label="Friendlane"></span><span class="s2" aria-label="Chirpwire"></span>
    <span class="s3" aria-label="Circleplus"></span><span class="s4" aria-label="Worknet"></span>
  </nav>
</header>

<section class="hero">
  <h1 class="hero-title">Promising An End Benefit</h1>
  <p class="hero-sub">Summarizing How to get it</p>
  <div class="hero-photo" role="img" aria-label="Photo of four smiling friends posing together"></div>

  <ul class="benefits">
    <li class="benefit b1">
      <span class="benefit-icon"><svg width="22" height="20" viewBox="0 0 22 20"><rect x="1" y="1" width="20" height="13" fill="none" stroke="#1a9ccc" stroke-width="2"/><path d="M7 18h8M11 14v4M6 11l8-8" stroke="#1a9ccc" stroke-width="2"/></svg></span>
      <h3>Sed do eiusmod tempor incididunt ut labore</h3>
      <p>Duis aute irure dolor in reprehenderit in voluptate velit esse cillum dolore eu fugiat nulla pariatur. Excepteur sint occaecat cupidatat non proident, sunt in culpa qui</p>
    </li>
    <li class="benefit b2">
      <span class="benefit-icon"><svg width="22" height="18" viewBox="0 0 22 18"><rect x="1" y="1" width="20" height="16" fill="none" stroke="#1a9ccc" stroke-width="2"/><path d="M1 5h20M8 8l-3 3 3 3M14 8l3 3-3 3" stroke="#1a9ccc" stroke-width="1.6" fill="none"/></svg></span>
      <h3>Sed do eiusmod tempor incididunt ut labore</h3>
      <p>Duis aute irure dolor in reprehenderit in voluptate velit esse cillum dolore eu fugiat nulla pariatur. Excepteur</p>
    </li>
    <li class="benefit">
      <span class="benefit-icon"><svg width="22" height="18" viewBox="0 0 22 18"><rect x="1" y="1" width="20" height="16" fill="none" stroke="#1a9ccc" stroke-width="2"/><path d="M1 5h20M8 7v8l7-4z" stroke="#1a9ccc" stroke-width="1.4" fill="#1a9ccc"/></svg></span>
      <h3>Sed do eiusmod tempor incididunt ut labore</h3>
      <p>Duis aute irure dolor in reprehenderit in voluptate velit esse cillum dolore eu fugiat nulla pariatur. Excepteur sint occaecat cupidatat non proident.</p>
    </li>
  </ul>

  <form class="signup" aria-label="Free membership sign-up">
    <svg class="signup-frame" width="466" height="430" viewBox="0 0 466 430">
      <path d="M1 13H305L320 1H465V429H1Z" fill="#fafafa" stroke="#cfd6da" stroke-width="2"/>
      <path d="M40 51H244L274 21" fill="none" stroke="#1a7fb5" stroke-width="1"/>
      <circle cx="274" cy="21" r="3" fill="#1a7fb5"/>
    </svg>
    <div class="signup-inner">
      <span class="signup-close">×</span>
      <h2 class="signup-title">Free Membership</h2>
      <p class="signup-lead"><span>Join the growing number of people who have discovered the</span><span>power and ease of Tallbrook.</span></p>
      <div class="field f1">First Name *<svg width="14" height="14" viewBox="0 0 14 14"><circle cx="7" cy="4" r="3.5" fill="#999"/><path d="M0 14c0-5 14-5 14 0z" fill="#999"/></svg></div>
      <div class="field f2">Last Name *<svg width="14" height="14" viewBox="0 0 14 14"><circle cx="7" cy="4" r="3.5" fill="#999"/><path d="M0 14c0-5 14-5 14 0z" fill="#999"/></svg></div>
      <div class="field f3">E-mail *<svg width="16" height="12" viewBox="0 0 16 12"><rect x=".5" y=".5" width="15" height="11" fill="none" stroke="#999"/><path d="M.5 .5l7.5 6 7.5-6M.5 11.5l5.5-5M15.5 11.5l-5.5-5" fill="none" stroke="#999"/></svg></div>
      <label class="choice c1"><i></i>I want to hire a freelancer</label>
      <label class="choice c2"><i></i>I am a freelancer</label>
      <div class="submit">Submit</div>
    </div>
  </form>
</section>

<section class="testimonial">
  <span class="quote-open">“</span>
  <div class="avatar" role="img" aria-label="Portrait of the reviewer"></div>
  <p class="quote-text">"Duis aute irure dolor in reprehenderit in voluptate velit esse cillum dolore eu fugia "</p>
  <p class="quote-author">Dorian Vell Ashcombe</p>
  <span class="quote-close">”</span>
</section>

<section class="abtest">
  <h2>Supercharge Your A/B Testing</h2>
  <p class="tag">Creating A/B Tests is Hard Work. Use Freelancers to Get More Done!</p>
  <svg class="steps" width="160" height="145" viewBox="0 0 160 145">
    <rect x="31" y="2" width="80" height="35" fill="#f39a4e"/><rect x="31" y="2" width="26" height="35" fill="#f7b57c"/>
    <rect x="31" y="37" width="100" height="34" fill="#f9c32e"/><rect x="31" y="37" width="26" height="34" fill="#fbd460"/>
    <rect x="31" y="71" width="125" height="36" fill="#3c9ccf"/><rect x="31" y="71" width="26" height="36" fill="#67b4dc"/>
    <rect x="31" y="107" width="150" height="36" fill="#f1f1f1" stroke="#ddd"/>
    <text x="84" y="29" fill="#fff" font-family="Ubuntu,sans-serif" font-size="17" font-weight="500">01</text>
    <text x="108" y="64" fill="#fff" font-family="Ubuntu,sans-serif" font-size="17" font-weight="500">02</text>
    <text x="132" y="99" fill="#fff" font-family="Ubuntu,sans-serif" font-size="17" font-weight="500">03</text>
  </svg>
  <span class="step-label" style="left:119px;top:59px">Get Innovative Ideas for Test Variations.</span>
  <span class="step-label" style="left:146px;top:93px">Crowdsource Killer Copy &amp; Creative</span>
  <span class="step-label" style="left:174px;top:129px">On-demand Code Support</span>
  <span class="step-label" style="left:199px;top:162px">Run More Tests, Get Results Faster</span>
</section>

<section class="partners" aria-label="Trusted by">
  <span style="left:162px">Corvane</span>
  <span style="left:313px">Deskline 365</span>
  <span style="left:466px">Brightpath</span>
  <span style="left:647px">Testwell</span>
  <span style="left:847px">Slidemark</span>
</section>

<footer class="site-footer">
  <div class="footer-rule"></div>
  <p class="copyright">Copyright © 2014 Tallbrook, Inc. Harlow Bay, CA | All Rights Reserved | <a href="#">Terms and Conditions</a> | <a href="#">Privacy Policy</a></p>
  <div class="footer-brand"><i></i><span>Tallbrook</span></div>
</footer>
</body>
</html>
```